Need help in designing new business card utilizing our new logo.

BuildMarq Solutions works with Construction Business Owners, Managers & IT Professionals to strengthen software usage and increase user productivity.

Our Construction Accounting and Mobile Field Management Software Clients engage with us in the following areas:

New Software Implementations
Software Re-Implementations
Redesigning Software Usage at the User Level
Project Coordination & Management
Continued Software Support

Old tag line:
Comparing Paths - Delivering Results

www.buildmarq-solutions.example

Stride 4 is a product, but not needed for a new business card.

```html
<!DOCTYPE html>
<html lang="en">
<head>
<meta charset="utf-8">
<title>BuildMarq Solutions – Business Card</title>
<link href="https://fonts.googleapis.com/css2?family=Roboto:wght@300;400;500;700&display=swap" rel="stylesheet">
<style>
  :root {
    --backdrop: #3a3b3e;
    --card: #20242c;
    --card-edge: #2a2f38;
    --brand-blue: #0d3f8f;
    --accent-blue: #2a66c9;
    --logo-grey: #b9bcc2;
    --text-light: #f2f3f5;
    --text-muted: #c7cad0;
  }
  * { box-sizing: border-box; margin: 0; padding: 0; }
  html, body { width: 799px; height: 1200px; overflow: hidden; }
  body {
    background: var(--backdrop);
    font-family: "Roboto", Arial, sans-serif;
    position: relative;
  }
  .card {
    position: absolute;
    left: 80px;
    width: 640px;
    height: 366px;
    background: var(--card);
    border: 1px solid var(--card-edge);
    border-radius: 18px;
    overflow: hidden;
    box-shadow: 0 10px 30px rgba(0,0,0,0.35);
  }
  .card--front { top: 90px; }
  .card--back { top: 640px; }

  /* Front */
  .front-brand {
    position: absolute;
    top: 52px; left: 0; right: 0;
    display: flex; justify-content: center; align-items: center; gap: 14px;
  }
  .brand-mark {
    width: 26px; height: 26px;
    background: var(--logo-grey);
  }
  .brand-name {
    font-weight: 500;
    font-size: 34px;
    letter-spacing: 1px;
    color: var(--logo-grey);
  }
  .service-band {
    position: absolute;
    top: 132px; left: 0; right: 0;
    height: 126px;
    background: var(--brand-blue);
    display: flex; flex-direction: column; justify-content: center; align-items: center;
    color: var(--text-light);
    font-size: 17px; font-weight: 400; line-height: 27px;
  }
  .front-web {
    position: absolute;
    top: 290px; left: 0; right: 0;
    display: flex; justify-content: center; align-items: center; gap: 22px;
    color: var(--text-light); font-size: 17px;
  }
  .rule {
    width: 42px; height: 2px; background: var(--text-muted);
  }

  /* Back */
  .back-brand {
    position: absolute;
    top: 64px; left: 48px;
  }
  .back-brand .brand-row { display: flex; align-items: center; gap: 12px; }
  .back-brand .brand-mark { width: 22px; height: 22px; background: var(--accent-blue); }
  .back-brand .brand-name { font-size: 28px; color: var(--accent-blue); }
  .tagline {
    margin-top: 6px; margin-left: 34px;
    font-size: 10px; color: var(--text-muted);
  }
  .person {
    position: absolute;
    top: 138px; left: 300px; right: 20px;
    color: var(--text-light);
  }
  .person-name { font-size: 26px; font-weight: 700; }
  .person-role { font-size: 14px; color: var(--text-muted); margin-bottom: 10px; }
  .contact-list { list-style: none; }
  .contact-list li {
    display: flex; align-items: center; gap: 10px;
    font-size: 14px; line-height: 22px; color: var(--text-light);
    white-space: nowrap;
  }
  .contact-list svg { width: 12px; height: 12px; fill: var(--accent-blue); flex: none; }
  .address {
    position: absolute;
    bottom: 30px; left: 48px;
    font-size: 16px; color: var(--text-light);
  }
  .corner-rule {
    position: absolute; height: 2px; width: 44px; background: var(--accent-blue);
  }
  .corner-rule--left { left: 24px; top: 240px; }
  .corner-rule--right { right: 30px; bottom: 22px; }
</style>
</head>
<body>

<section class="card card--front">
  <div class="front-brand">
    <span class="brand-mark"></span>
    <span class="brand-name">BuildMarq Solutions</span>
  </div>
  <div class="service-band">
    <p>New Software Implementations &nbsp;|&nbsp; Software Re-Implementations</p>
    <p>Redesigning Software Usage at the User Level</p>
    <p>Project Coordination &amp; Management &nbsp;|&nbsp; Continued Software Support</p>
  </div>
  <div class="front-web">
    <span class="rule"></span>
    <span>www.buildmarq-solutions.example</span>
    <span class="rule"></span>
  </div>
</section>

<section class="card card--back">
  <div class="back-brand">
    <div class="brand-row">
      <span class="brand-mark"></span>
      <span class="brand-name">BuildMarq Solutions</span>
    </div>
    <p class="tagline">Comparing Paths - Delivering Results</p>
  </div>

  <span class="corner-rule corner-rule--left"></span>

  <div class="person">
    <p class="person-name">Dana R. Whitfield</p>
    <p class="person-role">Owner</p>
    <ul class="contact-list">
      <li>
        <svg viewBox="0 0 12 12"><rect x="3" y="0" width="6" height="12" rx="1.2"/></svg>
        555-014-2290
      </li>
      <li>
        <svg viewBox="0 0 12 12"><path d="M2 1h3l1 3-1.5 1a7 7 0 0 0 2.5 2.5L8 6l3 1v3a1 1 0 0 1-1 1A9 9 0 0 1 1 2a1 1 0 0 1 1-1z"/></svg>
        555-010-4400 ext. 100
      </li>
      <li>
        <svg viewBox="0 0 12 12"><path d="M0 2h12v8H0z M0 2l6 4.5L12 2" /></svg>
        dana.whitfield@buildmarq-solutions.example
      </li>
      <li>
        <svg viewBox="0 0 12 12"><circle cx="6" cy="6" r="6"/></svg>
        www.buildmarq-solutions.example
      </li>
    </ul>
  </div>

  <p class="address">14B Harbor Lane - Suite 210 Millbrook, NY 10000</p>
  <span class="corner-rule corner-rule--right"></span>
</section>

</body>
</html>
```